Interior Design/ New Construction interior finishes

Interior Design Website

Target Market(s)

Home builders, New Construction, Renovations, Public

Industry/Entity Type

Construction

Coding

Coded - Design and coding required

Number of Pages Required

1 page

Font styles to use
Sans Serif

Colors

Designer to choose colors to be used in the design.

Requirements
Must have
• Section to upload pictures of projects
• Simple and modern design
• Designer 1 details about myself
• Logo
• Upload section for photos for future jobs
Nice to have
• Sections they can click on to see certain rooms in a house
• Decorating, floral arrangements, holiday decorating.
• I have lots of before and after as well. Maybe a section for those.

```html
<!DOCTYPE html>
<html lang="en">
<head>
<meta charset="utf-8">
<title>Linden Designs — Interior Design</title>
<link rel="stylesheet" href="https://fonts.googleapis.com/css2?family=Oswald:wght@400;500&family=PT+Sans:wght@400;700&display=swap">
<style>
:root{
  --accent:#9c8471;
  --accent-dark:#7d6757;
  --ink:#1d1d1d;
  --text:#555;
  --muted:#8a8a8a;
  --line:#d9d2cc;
  --paper:#ffffff;
  --mist:#efefee;
  --footer:#222222;
  --footer-bar:#151515;
}
*{box-sizing:border-box;margin:0;padding:0}
html,body{width:1200px;height:3403px;overflow:hidden;background:var(--paper)}
body{position:relative;font-family:"PT Sans",Arial,sans-serif;color:var(--text)}
.abs{position:absolute}
.photo{position:absolute}
.heading{font-family:"Oswald",Arial,sans-serif;font-weight:500;color:var(--ink);white-space:nowrap}
.heading .accent{color:var(--accent)}
.outline-btn{position:absolute;display:flex;align-items:center;justify-content:center;gap:8px;border:1px solid var(--accent);outline:1px solid var(--line);outline-offset:3px;font-size:11px;letter-spacing:1px;color:var(--accent-dark);text-transform:uppercase;font-weight:700;white-space:nowrap}
.body-copy{font-size:13px;line-height:20px;color:var(--text)}

/* Hero */
.hero{position:absolute;left:0;top:0;width:1200px;height:620px;overflow:hidden}
.hero-photo{width:1200px;height:620px;left:0;top:0;background:linear-gradient(135deg,#8f8a84 0%,#6d6660 40%,#4f4a45 70%,#6b6a6c 100%)}
.hero-shade{left:0;top:0;width:1200px;height:620px;background:rgba(30,30,30,.25)}
.brand{left:200px;top:20px;display:flex;flex-direction:column;align-items:center;gap:6px}
.brand-mark{width:50px;height:50px;border:1.5px solid var(--ink);border-radius:50%}
.brand-name{font-family:"PT Sans",Arial,sans-serif;font-size:19px;letter-spacing:3px;color:var(--ink);white-space:nowrap}
.topbar{right:200px;top:33px;display:flex;gap:20px;font-size:11px;color:#fff;align-items:center}
.topbar span{display:flex;align-items:center;gap:6px}
.nav{right:200px;top:70px;display:flex;gap:44px;font-family:"Oswald",Arial,sans-serif;font-size:13px;color:#fff}
.hero-icon{left:940px;top:238px}
.hero-title{right:200px;top:306px;font-family:"Oswald",Arial,sans-serif;font-weight:500;font-size:44px;color:#fff;letter-spacing:.5px;white-space:nowrap}
.hero-text{right:200px;top:390px;width:560px;text-align:right;font-size:13px;line-height:26px;color:#fff;font-weight:700}
.hero-btn{left:841px;top:484px;width:157px;height:48px;border:1.5px solid #fff;display:flex;align-items:center;justify-content:center;font-family:"Oswald",Arial,sans-serif;color:#fff;font-size:14px;outline:1px solid rgba(255,255,255,.6);outline-offset:-6px}
.dots{left:966px;top:563px;display:flex;gap:5px}
.dots i{width:7px;height:7px;border-radius:50%;background:#fff;display:block;opacity:.6}
.dots i:first-child{opacity:1}

/* About */
.about-title{left:200px;top:736px;font-size:38px}
.about-copy{left:200px;top:812px;width:400px}
.about-btn{left:200px;top:924px;width:140px;height:38px}
.about-visual{left:658px;top:698px}
.panel-brand{left:942px;top:760px;width:240px;display:flex;flex-direction:column;align-items:center;gap:6px;color:#fff;text-align:center}
.panel-brand .brand-mark{border-color:#fff;width:56px;height:56px}
.panel-brand .brand-name{color:#fff;font-size:21px}
.panel-brand p{font-size:10px;line-height:15px;margin-top:14px}

/* Projects */
.projects{left:0;top:1020px;width:1200px;height:772px;background:linear-gradient(180deg,#f2f2f1 0%,#ebeae8 60%,#f3f3f2 100%)}
.section-rule{position:absolute;top:1134px;height:2px;background:var(--ink);width:100px}
.projects-title{left:0;width:1200px;text-align:center;top:1110px;font-size:34px}
.feature-card{left:200px;top:1209px;width:394px;height:406px;background:#fff}
.feature-card .photo{left:0;top:0;width:394px;height:200px;background:linear-gradient(180deg,#9fb3c4 0%,#b19a7d 55%,#5e8ca8 100%)}
.feature-card h3{position:absolute;left:16px;top:220px;font-family:"Oswald",Arial,sans-serif;font-weight:500;font-size:14px;color:var(--ink)}
.feature-card .kicker{position:absolute;left:16px;top:260px;font-size:11px;color:#444;text-transform:uppercase}
.feature-card .note{position:absolute;left:16px;top:290px;width:330px;font-size:10px;line-height:16px;color:var(--muted)}
.feature-card .dark-btn{position:absolute;left:16px;top:346px;width:160px;height:34px;background:#111;color:#fff;font-size:10px;font-weight:700;display:flex;align-items:center;justify-content:center}
.thumb{width:186px;height:198px}
.slider-arrows{left:576px;top:1663px;display:flex;gap:4px}
.slider-arrows span{width:20px;height:20px;border-radius:50%;background:#111;display:flex;align-items:center;justify-content:center}

/* Before / after */
.ba-visual{left:0;top:1792px}
.ba-label{font-family:"Oswald",Arial,sans-serif;color:#fff;font-size:19px;font-weight:500}
.ba-title{right:200px;top:1832px;font-size:31px;text-align:right}
.ba-copy{left:580px;top:1904px;width:420px;text-align:right}
.ba-btn{left:857px;top:2022px;width:143px;height:38px}

/* Gallery */
.gallery-title{left:0;width:1200px;text-align:center;top:2176px;font-size:36px}
.g-item{position:absolute;width:233px}
.g-item .photo{position:relative;width:233px}
.g-item p{font-size:13px;line-height:20px;color:var(--ink);margin-top:12px;width:233px}
.g-item .details{display:flex;align-items:center;gap:10px;margin-top:8px;font-size:13px;color:var(--accent)}
.g-item .details::before{content:"";width:34px;height:2px;background:var(--accent)}
.floral-tag{position:absolute;left:0;top:0;width:233px;height:212px;display:flex;flex-direction:column;align-items:center;justify-content:center;color:#fff;font-family:"Oswald",Arial,sans-serif;font-size:13px;gap:4px}
.floral-tag b{font-size:30px;font-weight:400;line-height:30px}
.upload-btn{left:467px;top:3050px;width:266px;height:44px}

/* Footer */
.footer{left:0;top:3159px;width:1200px;height:198px;background:var(--footer)}
.footer-bar{left:0;top:3357px;width:1200px;height:46px;background:var(--footer-bar);font-size:10px;color:#999}
.f-head{font-family:"Oswald",Arial,sans-serif;font-weight:400;font-size:20px;color:#fff;white-space:nowrap}
.f-line{display:flex;align-items:center;gap:12px;font-size:12px;color:#aaa}
.f-sub{font-size:10px;letter-spacing:1px;color:#888;text-transform:uppercase;white-space:nowrap}
.social{display:flex;gap:18px}
.social i{width:12px;height:12px;border-radius:50%;background:#ddd;display:block}
.news-input{width:196px;height:36px;background:#3a3a3a;color:#888;font-size:10px;display:flex;align-items:center;padding-left:18px}
.news-btn{width:106px;height:36px;background:var(--accent);color:#fff;font-size:11px;font-weight:700;display:flex;align-items:center;justify-content:center}
.bar-links{left:200px;top:17px;display:flex;gap:12px}
.bar-links span+span::before{content:"|";margin-right:12px;color:#666}
</style>
</head>
<body>

<!-- Hero -->
<section class="hero">
  <div class="photo hero-photo" role="img" aria-label="Bright living room with white sofas, a rustic wooden coffee table and a vase of purple flowers"></div>
  <div class="abs hero-shade"></div>
  <svg class="abs" width="1200" height="620" style="left:0;top:0">
    <polygon points="0,0 442,0 0,488" fill="#fff"/>
    <polygon points="0,488 0,620 100,620" fill="#fff"/>
    <polygon points="1000,620 1200,620 1200,520" fill="#fff"/>
  </svg>
  <div class="abs brand">
    <div class="brand-mark"></div>
    <div class="brand-name">Linden Designs</div>
  </div>
  <div class="abs topbar">
    <span><svg width="11" height="11" viewBox="0 0 24 24"><path fill="#fff" d="M6.6 10.8a15.1 15.1 0 0 0 6.6 6.6l2.2-2.2c.3-.3.7-.4 1-.2 1.1.4 2.3.6 3.6.6.6 0 1 .4 1 1V20c0 .6-.4 1-1 1A17 17 0 0 1 3 4c0-.6.4-1 1-1h3.5c.6 0 1 .4 1 1 0 1.200.2 2.4.6 3.6.1.3 0 .7-.2 1z"/></svg>+1 555 0134</span>
    <span><svg width="12" height="10" viewBox="0 0 24 18"><rect x="1" y="1" width="22" height="16" fill="none" stroke="#fff" stroke-width="2"/><path d="M1 1l11 9 11-9" fill="none" stroke="#fff" stroke-width="2"/></svg>hello@lindendesigns.com</span>
  </div>
  <nav class="abs nav">
    <span>Home</span><span>About Me</span><span>Services</span><span>Projects</span><span>Gallery</span><span>Contact Us</span>
  </nav>
  <svg class="abs hero-icon" width="56" height="52" viewBox="0 0 56 52"><path d="M28 3 3 26h8v23h34V26h8z" fill="#fff"/><rect x="23" y="30" width="10" height="19" fill="#5a544f"/></svg>
  <h1 class="abs hero-title">WELCOME TO LINDEN DESIGNS</h1>
  <p class="abs hero-text">Lorem Ipsum is simply dummy text of the printing and typesetting industry. Lorem Ipsum has<br>been the industry's standard dummy text</p>
  <div class="abs hero-btn">CONTACT US</div>
  <div class="abs dots"><i></i><i></i><i></i></div>
</section>

<!-- About -->
<h2 class="abs heading about-title">About <span class="accent">Me</span></h2>
<p class="abs body-copy about-copy">Lorem Ipsum is simply dummy text of the printing and typesetting industry Lorem Ipsum has been the industry's standard dummy text ever since the 1500s, when an unknown printer took a galley of type and scrambled it to make a type specimen book.</p>
<div class="outline-btn about-btn">Read more <span>→</span></div>
<svg class="abs about-visual" width="542" height="318" role="img" aria-label="Open plan living room with tall windows, warm wooden ceiling and brown leather sofas">
  <defs><linearGradient id="aboutPhoto" x1="0" y1="0" x2="1" y2="1"><stop offset="0" stop-color="#b7a58d"/><stop offset=".5" stop-color="#7d5f44"/><stop offset="1" stop-color="#4d3a2c"/></linearGradient></defs>
  <polygon points="0,159 91,0 542,0 542,318 91,318" fill="url(#aboutPhoto)"/>
  <polygon points="262,0 542,0 542,318 262,318 170,159" fill="#a08a78"/>
</svg>
<div class="abs panel-brand">
  <div class="brand-mark"></div>
  <div class="brand-name">Linden Designs</div>
  <p>Lorem Ipsum is simply dummy text of the printing<br>and typesetting industry Lorem Ipsum</p>
</div>

<!-- Projects -->
<section class="abs projects" role="img" aria-label="Faded bright interior with large glass doors as backdrop"></section>
<div class="section-rule" style="left:395px"></div>
<div class="section-rule" style="left:705px"></div>
<h2 class="abs heading projects-title">MY <span class="accent">Projects</span></h2>
<article class="abs feature-card">
  <div class="photo" role="img" aria-label="Stone house with a swimming pool and garden"></div>
  <h3>Decorating</h3>
  <div class="kicker">Lorem Ipsum is simply dummy text of the printing</div>
  <p class="note">Lorem Ipsum is simply dummy text of the printing and typesetting industry lorem ipsum text....</p>
  <div class="dark-btn">SEE CERTAIN ROOMS</div>
</article>
<div class="photo thumb" style="left:612px;top:1209px;background:linear-gradient(180deg,#d4d2cf,#8e8a86)" role="img" aria-label="White bathroom with freestanding tub"></div>
<div class="photo thumb" style="left:815px;top:1209px;background:linear-gradient(180deg,#e1ddd6,#9a8f83)" role="img" aria-label="Bright living room with wooden table"></div>
<div class="photo thumb" style="left:612px;top:1417px;background:linear-gradient(180deg,#a88e72,#5f4b3c)" role="img" aria-label="Breakfast nook with round table"></div>
<div class="photo thumb" style="left:815px;top:1417px;background:linear-gradient(180deg,#6a6865,#3d3b39)" role="img" aria-label="Dark kitchen sink detail">
  <svg class="abs" style="left:78px;top:84px" width="30" height="30" viewBox="0 0 30 30"><circle cx="15" cy="15" r="14" fill="none" stroke="#fff" stroke-width="1.5"/><path d="M11 19l8-8M12 14l-2 2a3 3 0 0 0 4 4l2-2M18 16l2-2a3 3 0 0 0-4-4l-2 2" fill="none" stroke="#fff" stroke-width="1.5"/></svg>
</div>
<div class="abs slider-arrows">
  <span><svg width="8" height="8" viewBox="0 0 8 8"><path d="M5.5 1 2.5 4l3 3" fill="none" stroke="#fff" stroke-width="1.6"/></svg></span>
  <span><svg width="8" height="8" viewBox="0 0 8 8"><path d="M2.5 1l3 3-3 3" fill="none" stroke="#fff" stroke-width="1.6"/></svg></span>
</div>

<!-- Before and after -->
<svg class="abs ba-visual" width="545" height="317" role="img" aria-label="Before and after of a white bathroom renovation">
  <defs><linearGradient id="afterPhoto" x1="0" y1="0" x2="1" y2="1"><stop offset="0" stop-color="#f2f2f2"/><stop offset="1" stop-color="#b9b9b9"/></linearGradient></defs>
  <polygon points="0,0 430,0 545,158 430,317 0,317" fill="url(#afterPhoto)"/>
  <polygon points="0,0 300,0 170,317 0,317" fill="#3f3f3f"/>
  <polygon points="300,0 430,0 545,158 430,317 170,317" fill="#000" opacity=".08"/>
</svg>
<div class="abs ba-label" style="left:120px;top:1934px">BEFORE</div>
<div class="abs ba-label" style="left:358px;top:1934px">AFTER</div>
<h2 class="abs heading ba-title">Interiors Designed <span class="accent">by Linden Designs</span></h2>
<p class="abs body-copy ba-copy">Lorem Ipsum is simply dummy text of the printing and typesetting industry. Lorem Ipsum has been the industry's standard dummy text ever since the 1500s, when an unknown printer took a galley of type and scrambled it to make a type specimen book.</p>
<div class="outline-btn ba-btn">View more <span>→</span></div>

<!-- Gallery -->
<h2 class="abs heading gallery-title"><span class="accent">Gallery</span></h2>
<div class="g-item" style="left:200px;top:2295px">
  <div class="photo" style="height:212px;background:linear-gradient(180deg,#b08d6b,#6e5642)" role="img" aria-label="Dining area with chandelier"></div>
  <p>Lorem Ipsum is simply dummy text of the printing and typesetting..</p><div class="details">Details</div>
</div>
<div class="g-item" style="left:483px;top:2268px">
  <div class="photo" style="height:306px;background:linear-gradient(180deg,#d8cdbd,#9d8f80)" role="img" aria-label="Wooden framed mirror above a console with flowers"></div>
  <p>Lorem Ipsum is simply dummy text of the printing and typesetting..</p><div class="details">Details</div>
</div>
<div class="g-item" style="left:767px;top:2295px">
  <div class="photo" style="height:212px;background:linear-gradient(180deg,#6b645d,#3c3733)" role="img" aria-label="Hallway interior, floral arrangements category"></div>
  <div class="floral-tag"><b>+</b>FLORAL ARRANGEMENTS</div>
  <p>Lorem Ipsum is simply dummy text of the printing and typesetting..</p><div class="details">Details</div>
</div>
<div class="g-item" style="left:200px;top:2615px">
  <div class="photo" style="height:304px;background:linear-gradient(180deg,#d7d6d3,#7d7670)" role="img" aria-label="Dining room with grey chairs and wooden table"></div>
  <p>Lorem Ipsum is simply dummy text of the printing and typesetting..</p><div class="details">Details</div>
</div>
<div class="g-item" style="left:483px;top:2681px">
  <div class="photo" style="height:210px;background:linear-gradient(180deg,#9c8b78,#564a40)" role="img" aria-label="Bathroom with freestanding tub and chandelier"></div>
  <p>Lorem Ipsum is simply dummy text of the printing and typesetting..</p><div class="details">Details</div>
</div>
<div class="g-item" style="left:767px;top:2615px">
  <div class="photo" style="height:304px;background:linear-gradient(180deg,#e4e2de,#8c8680)" role="img" aria-label="Breakfast nook with iron chandelier and upholstered chairs"></div>
  <p>Lorem Ipsum is simply dummy text of the printing and typesetting..</p><div class="details">Details</div>
</div>
<div class="outline-btn upload-btn">Upload pictures of project <span>→</span></div>

<!-- Footer -->
<footer class="abs footer">
  <div class="abs f-head" style="left:200px;top:46px">Contact Us</div>
  <div class="abs f-line" style="left:200px;top:94px"><svg width="12" height="12" viewBox="0 0 24 24"><path fill="#aaa" d="M6.6 10.8a15.1 15.1 0 0 0 6.6 6.6l2.2-2.2c.3-.3.7-.4 1-.2 1.1.4 2.3.6 3.6.6.6 0 1 .4 1 1V20c0 .6-.4 1-1 1A17 17 0 0 1 3 4c0-.6.4-1 1-1h3.5c.6 0 1 .4 1 1 0 1.2.2 2.4.6 3.6.1.3 0 .7-.2 1z"/></svg>+1 555 0134</div>
  <div class="abs f-line" style="left:200px;top:126px"><svg width="13" height="10" viewBox="0 0 24 18"><rect x="1" y="1" width="22" height="16" fill="none" stroke="#aaa" stroke-width="2"/><path d="M1 1l11 9 11-9" fill="none" stroke="#aaa" stroke-width="2"/></svg>hello@lindendesigns.com</div>
  <div class="abs f-head" style="left:424px;top:46px">Connect With Us</div>
  <div class="abs f-sub" style="left:436px;top:80px">Social Media Channels</div>
  <div class="abs social" style="left:446px;top:102px"><i></i><i></i><i></i><i></i></div>
  <div class="abs f-head" style="left:688px;top:46px">Newsletter</div>
  <div class="abs f-sub" style="left:688px;top:80px">Sign up for special offers</div>
  <div class="abs" style="left:688px;top:106px;display:flex;gap:10px"><div class="news-input">EMAIL</div><div class="news-btn">SUBSCRIBE</div></div>
</footer>
<div class="abs footer-bar">
  <div class="abs bar-links"><span>Home</span><span>About Us</span><span>Services</span><span>Projects</span><span>Gallery</span><span>Contact Us</span></div>
  <div class="abs" style="right:200px;top:17px">© Copyright 2018 Linden Designs. All Rights Reserved.</div>
</div>

</body>
</html>
```